Business Card for a recruitment agency specializing in engineers and geeks.

I am looking to create Business Card Design for my company.
That
## Company name:
Vornplick Inc.
Vornplick is a term coined from the following concepts.
1. geek + engineer
2. geek utopia
## Company Description:
The concept of the company is to be a recruitment agency that creates a paradise for geeky engineers. We want to be a place where engineers can have more freedom and ideal career support.
# Target.
The noun itself is often given to companies that want to hire engineers, geeks, and IT-related personnel, so it would be nice to get the impression that this company seems to have good engineers and IT personnel. There are many occasions where I meet with the human resources department, president, or senior management and give it to them.
# Atmosphere
We are happy with simplicity, but with an impact that will help people remember the company. The logo is based on a dinosaur that does programming, so it should be somewhat playful, but since it will basically be used in a business setting, please don't make it too silly.
# About the logo
See the attached files. The company logo represents our engineers smiling upward because of our work, with the motif of a dinosaur doing programming.
## Color
We will leave the color scheme to you, but since the logo is in black and white, colors with such a taste would fit well.
## file format
ai, psd, png, svg
Industry/Entity Type
human resource and employment agency
Contact Information for Business Card
Company name, address, email, tel, URL,logo
Colors
Designer to choose colors to be used in the design.
Look and feel
Each slider illustrates characteristics of the customer's brand and the style your logo design should communicate.

```html
<!DOCTYPE html>
<html lang="en">
<head>
<meta charset="utf-8">
<title>Vornplick Inc. — Business Card</title>
<link rel="stylesheet" href="https://fonts.googleapis.com/css2?family=Open+Sans:wght@400;600;700&display=swap">
<style>
  :root {
    --canvas-bg: #d9d9d9;
    --card-white: #ffffff;
    --card-black: #1c1c1c;
    --ink: #111111;
    --accent-blue: #1ea7e1;
    --faint-grey: #ececec;
    --silver: #e6e6e6;
  }
  * { margin: 0; padding: 0; box-sizing: border-box; }
  html, body { width: 1200px; height: 800px; overflow: hidden; }
  body {
    background: var(--canvas-bg);
    font-family: "Open Sans", Arial, sans-serif;
    display: flex;
    align-items: center;
    justify-content: center;
    gap: 40px;
  }
  .card {
    position: relative;
    width: 520px;
    height: 298px;
    border-radius: 24px;
    overflow: hidden;
    border-bottom: 4px solid var(--accent-blue);
  }
  .card-front { background: var(--card-white); }
  .card-back { background: var(--card-black); }

  .brand-faint {
    position: absolute;
    left: 40px;
    bottom: 20px;
    width: 190px;
    height: 190px;
    background: var(--faint-grey);
    border-radius: 10px;
  }
  .brand-lockup {
    position: absolute;
    top: 56px;
    right: 48px;
    display: flex;
    align-items: center;
    gap: 12px;
  }
  .brand-mark {
    width: 26px;
    height: 26px;
    background: var(--ink);
    border-radius: 3px;
  }
  .brand-name {
    font-size: 34px;
    font-weight: 700;
    color: var(--ink);
    letter-spacing: 0.5px;
  }
  .address {
    position: absolute;
    right: 48px;
    top: 150px;
    text-align: right;
    font-size: 13px;
    line-height: 1.5;
    color: var(--ink);
  }
  .contact-block {
    position: absolute;
    left: 70px;
    bottom: 40px;
  }
  .contact-brace {
    position: absolute;
    left: -40px;
    top: 22px;
    width: 40px;
    height: 110px;
  }
  .person-name {
    font-size: 20px;
    font-weight: 700;
    color: var(--ink);
    letter-spacing: 0.5px;
  }
  .person-title {
    font-size: 14px;
    color: var(--accent-blue);
    margin-bottom: 10px;
  }
  .contact-list { list-style: none; }
  .contact-item {
    display: flex;
    align-items: center;
    gap: 10px;
    font-size: 13.5px;
    line-height: 1.65;
    color: var(--ink);
  }
  .contact-icon { width: 12px; height: 12px; flex: none; }

  .back-lockup {
    position: absolute;
    inset: 0;
    display: flex;
    align-items: center;
    justify-content: center;
    gap: 14px;
  }
  .back-mark {
    width: 30px;
    height: 30px;
    background: var(--silver);
    border-radius: 3px;
  }
  .back-name {
    font-size: 46px;
    font-weight: 700;
    color: var(--silver);
    letter-spacing: 0.5px;
  }
</style>
</head>
<body>

<section class="card card-front" aria-label="Business card front">
  <div class="brand-faint" aria-hidden="true"></div>

  <div class="brand-lockup">
    <span class="brand-mark" aria-hidden="true"></span>
    <span class="brand-name">Vornplick</span>
  </div>

  <p class="address">4120 Quillmere Road<br>Fenwick, Oregon 97031</p>

  <div class="contact-block">
    <svg class="contact-brace" viewBox="0 0 40 110" aria-hidden="true">
      <path d="M30 2 C14 2 16 20 16 40 C16 52 12 56 4 58 C12 60 16 64 16 76 C16 96 14 108 38 108"
            fill="none" stroke="var(--accent-blue)" stroke-width="2.5" stroke-linecap="round"/>
    </svg>
    <p class="person-name">DORIAN VELLOWAY</p>
    <p class="person-title">President</p>
    <ul class="contact-list">
      <li class="contact-item">
        <svg class="contact-icon" viewBox="0 0 12 12" aria-hidden="true"><path d="M2.5 1 L4.5 1 L5 3.5 L3.8 4.4 C4.4 6 5.9 7.6 7.6 8.2 L8.5 7 L11 7.5 L11 9.5 C11 10.3 10.3 11 9.5 11 C5 11 1 7 1 2.5 C1 1.7 1.7 1 2.5 1 Z" fill="var(--accent-blue)"/></svg>
        555-301-7284
      </li>
      <li class="contact-item">
        <svg class="contact-icon" viewBox="0 0 12 12" aria-hidden="true"><rect x="0.5" y="2" width="11" height="8" rx="1" fill="var(--accent-blue)"/><path d="M1 2.6 L6 6.5 L11 2.6" fill="none" stroke="#fff" stroke-width="1"/></svg>
        velloway@vornplick.com
      </li>
      <li class="contact-item">
        <svg class="contact-icon" viewBox="0 0 12 12" aria-hidden="true"><circle cx="6" cy="6" r="5.5" fill="var(--accent-blue)"/><path d="M0.5 6 H11.5 M6 0.5 C3.5 3 3.5 9 6 11.5 M6 0.5 C8.5 3 8.5 9 6 11.5" fill="none" stroke="#fff" stroke-width="0.8"/></svg>
        www.vornplick.com
      </li>
    </ul>
  </div>
</section>

<section class="card card-back" aria-label="Business card back">
  <div class="back-lockup">
    <span class="back-mark" aria-hidden="true"></span>
    <span class="back-name">Vornplick</span>
  </div>
</section>

</body>
</html>
```